Floxaro Poster Design (A3 or larger) for exhibition

I need 3 posters done for an exhibition I have. Each poster should be able to be printed in A3 or larger. Each poster should describe a machine type that we are selling. I have done 3 word documents for each machine with the written text. Don't worry about the format in the Word document - use whatever format and font you think looks good.
The 3 machine types are:
- quorel
- tandoro
- Venrik
These all have to be on separate posters. don't put all these machines on the one page. I have provided images for each machine (each image has the name of the relevant machine in the file name). Make sure you only use the images for the relevant machine in each poster. I don't mind if you pick only one image for each machine to use or all of them - up to you.
Look and feel
Each slider illustrates characteristics of the customer's brand and the style your logo design should communicate.

```html
<!DOCTYPE html>
<html lang="en">
<head>
<meta charset="utf-8">
<title>Floxaro – Quorel Poster</title>
<link rel="stylesheet" href="https://fonts.googleapis.com/css2?family=Anton&family=Open+Sans:wght@400;600;700&family=Oswald:wght@500;700&display=swap">
<style>
  :root {
    --ink: #0a0c10;
    --blue: #1fb4ec;
    --blue-deep: #0d8cc4;
    --text: #e9eef2;
    --muted: #c9d3da;
    --photo-a: #e4e8ec;
    --photo-b: #2a6fb2;
  }
  * { margin: 0; padding: 0; box-sizing: border-box; }
  html, body { width: 900px; height: 1200px; overflow: hidden; background: #1a1a1a; }
  .poster {
    position: relative; width: 900px; height: 1200px; overflow: hidden;
    background: radial-gradient(ellipse at 50% 40%, #1b2129 0%, var(--ink) 70%);
    font-family: "Open Sans", Arial, sans-serif; color: var(--text);
  }
  .header-stripes { position: absolute; left: 0; top: 0; z-index: 2; }
  .title-band {
    position: absolute; right: 0; top: 28px; width: 390px; height: 104px; z-index: 2;
    background: var(--blue); display: flex; align-items: center; padding-left: 34px;
  }
  .title-band h1 {
    font-family: "Anton", Impact, sans-serif; font-weight: 400; font-size: 86px;
    letter-spacing: 4px; color: #fff; line-height: 1;
  }
  .tagline {
    position: absolute; left: 520px; top: 160px; width: 350px; z-index: 3;
    font-size: 21px; line-height: 1.28; color: #fff;
  }
  .machine-photo {
    position: absolute; left: 70px; top: 250px; width: 760px; height: 510px; z-index: 1;
    background: radial-gradient(ellipse at 50% 55%, var(--photo-a) 0%, #9aa9b6 30%, var(--photo-b) 55%, rgba(18,22,28,0) 78%);
  }
  .divider { position: absolute; left: 0; top: 772px; width: 900px; height: 4px; background: var(--blue); }
  .features { position: absolute; left: 44px; top: 800px; width: 380px; }
  .features h2 { font-size: 30px; font-weight: 400; margin-bottom: 18px; }
  .features p { font-size: 17px; line-height: 1.35; color: var(--muted); margin-bottom: 22px; }
  .comparison { position: absolute; left: 470px; top: 818px; width: 400px; }
  .comparison h2 {
    font-family: "Oswald", Arial, sans-serif; font-weight: 700; font-size: 40px;
    letter-spacing: 1px; text-transform: uppercase; color: #fff;
    border-bottom: 4px solid var(--blue); padding-bottom: 4px; margin-bottom: 12px;
  }
  .spec-table { width: 100%; border-collapse: separate; border-spacing: 0 6px; font-size: 13px; }
  .spec-table th {
    width: 46%; text-align: left; vertical-align: top; padding: 6px 10px;
    background: var(--blue); color: var(--ink); font-family: "Oswald", Arial, sans-serif;
    font-weight: 500; text-transform: uppercase; letter-spacing: .5px;
  }
  .spec-table td { padding: 6px 10px; background: var(--blue-deep); color: #fff; line-height: 1.35; }
  .spec-table tr.gap th, .spec-table tr.gap td { background: transparent; }
</style>
</head>
<body>
<div class="poster">
  <svg class="header-stripes" width="520" height="150" viewBox="0 0 520 150" aria-hidden="true">
    <polygon points="300,0 340,0 200,150 160,150" fill="#1fb4ec"/>
    <polygon points="355,0 395,0 255,150 215,150" fill="#1fb4ec"/>
    <polygon points="410,0 430,0 290,150 270,150" fill="#0d8cc4"/>
  </svg>
  <div class="title-band"><h1>QUOREL</h1></div>
  <p class="tagline">The perfect low cost machine for your service station, car dealership or workshop</p>

  <div class="machine-photo" role="img" aria-label="Photograph of the Quorel rollover car wash machine with blue brushes"></div>
  <div class="divider"></div>

  <section class="features">
    <h2>Key features are:</h2>
    <p>versatility and is available in two versions - single-programme or multi-programme;</p>
    <p>high-quality engineering, construction and technology that ensures reliability, durability, and flawless results;</p>
    <p>added value by the optional installation of high pressure and the SWAYLINE system that governs the movement of the polyethylene, Fibrelux, or Plush Contact brushes for wrap-around washing of cars, vans and utes</p>
  </section>

  <section class="comparison">
    <h2>Comparison Table</h2>
    <table class="spec-table">
      <tr><th>Cars per hour</th><td>9 to 12 cars per hour</td></tr>
      <tr><th>Space required</th><td>9m</td></tr>
      <tr><th>Industry</th><td>Car dealerships, rental car companies, repair workshops, small petrol stations, DIY car wash sites</td></tr>
      <tr class="gap"><th></th><td></td></tr>
      <tr><th>Options</th><td>Tire blower drying, wheel brush program, pre-wash, chemical applicator, underbody wash</td></tr>
    </table>
  </section>
</div>
</body>
</html>
```